Business Card Design & logo

Residential building renovation and maintenance work.
All carpentry and joinery needs.
Laying solid timber and floating floors.
Kitchen and bathroom makeovers and modifications.
Interior fitouts,
small job specialist. tiling, plastering, painting,

I would like a silver background. With the use of different shades of grey, rustic orange, black and white.
I do not want pictures of hammers, chisels etc. I am looking for a logo to be incorporated into the card.

Carpentry

Contact Information for Business Card

BTQ Renovations and Maintenance
Lewis Tolbane
0471852036
info@btqfixes.com.au
btqfixes.com.au

```html
<!DOCTYPE html>
<html lang="en">
<head>
<meta charset="utf-8">
<title>BTQ Renovations and Maintenance – Business Card</title>
<link rel="stylesheet" href="https://fonts.googleapis.com/css2?family=Open+Sans:wght@400;600;700&display=swap">
<style>
  :root {
    --stage: #d9d6d2;
    --silver-light: #f4f4f4;
    --silver-mid: #dedede;
    --silver-dark: #bdbdbd;
    --charcoal: #4a4a4a;
    --charcoal-deep: #3c3c3c;
    --graphic-light: #6e6e6e;
    --graphic-dark: #484848;
    --ink: #111111;
    --white: #ffffff;
  }
  * { box-sizing: border-box; margin: 0; padding: 0; }
  html, body {
    width: 1200px; height: 885px; overflow: hidden;
    background: var(--stage);
    font-family: "Open Sans", Arial, sans-serif;
  }
  .canvas {
    position: relative; width: 1200px; height: 885px;
    display: flex; flex-direction: column; align-items: center; justify-content: center; gap: 45px;
  }
  .card {
    position: relative; width: 700px; height: 400px; border-radius: 4px; overflow: hidden;
    box-shadow: 0 6px 18px rgba(0,0,0,.25);
  }
  /* Front */
  .card-front {
    background: linear-gradient(135deg, var(--silver-light) 0%, var(--silver-mid) 55%, var(--silver-dark) 100%);
    color: var(--ink);
  }
  .front-graphic {
    position: absolute; left: 0; bottom: 0; width: 330px; height: 250px;
    background: linear-gradient(150deg, var(--graphic-light) 0%, var(--graphic-dark) 100%);
    border-top-right-radius: 6px;
  }
  .front-text {
    position: absolute; left: 360px; right: 30px; top: 36px;
  }
  .company-name {
    font-weight: 700; font-size: 27px; line-height: 1.15;
  }
  .person-name {
    margin-top: 52px; font-weight: 600; font-size: 24px;
  }
  .contact-list { list-style: none; margin-top: 40px; }
  .contact-list li {
    display: flex; align-items: center; gap: 10px; font-size: 18px; line-height: 1.55;
  }
  .contact-icon {
    width: 17px; height: 17px; background: var(--ink); border-radius: 2px;
    display: inline-flex; align-items: center; justify-content: center; flex-shrink: 0;
  }
  .contact-icon svg { width: 12px; height: 12px; }
  /* Back */
  .card-back {
    background: linear-gradient(135deg, var(--charcoal) 0%, var(--charcoal-deep) 100%);
    color: var(--white);
  }
  .brand-lockup {
    position: absolute; left: 60px; top: 50px; display: flex; align-items: center; gap: 22px;
  }
  .brand-mark { width: 64px; height: 64px; background: var(--white); }
  .brand-name { font-weight: 700; font-size: 27px; line-height: 1.15; }
  .services {
    position: absolute; left: 40px; right: 40px; top: 170px;
    list-style: none; text-align: center; font-weight: 600; font-size: 19px; line-height: 1.55;
  }
</style>
</head>
<body>
<main class="canvas">
  <section class="card card-front">
    <div class="front-graphic" role="img" aria-label="Large bold grey brand graphic in the lower left corner"></div>
    <div class="front-text">
      <h1 class="company-name">BTQ Renovations<br>And Maintenance</h1>
      <p class="person-name">Lewis Tolbane</p>
      <ul class="contact-list">
        <li><span class="contact-icon"><svg viewBox="0 0 12 12"><path d="M3 1.5l1.6 2.4-1 1a6 6 0 0 0 3 3l1-1L10 8.5 9 10.5C5 10 2 7 1.5 3z" fill="#fff"/></svg></span>0471852036</li>
        <li><span class="contact-icon"><svg viewBox="0 0 12 12"><circle cx="6" cy="6" r="4.5" fill="none" stroke="#fff" stroke-width="1.2"/><path d="M1.5 6h9M6 1.5c-2.5 3-2.5 6 0 9M6 1.5c2.5 3 2.5 6 0 9" fill="none" stroke="#fff" stroke-width="1"/></svg></span>btqfixes.com.au</li>
        <li><span class="contact-icon"><svg viewBox="0 0 12 12"><rect x="1.5" y="3" width="9" height="6.5" fill="none" stroke="#fff" stroke-width="1.1"/><path d="M1.5 3L6 7l4.5-4" fill="none" stroke="#fff" stroke-width="1.1"/></svg></span>info@btqfixes.com.au</li>
      </ul>
    </div>
  </section>

  <section class="card card-back">
    <div class="brand-lockup">
      <span class="brand-mark" aria-hidden="true"></span>
      <h2 class="brand-name">BTQ Renovations<br>And Maintenance</h2>
    </div>
    <ul class="services">
      <li>All carpentry and joinery needs</li>
      <li>Laying solid timber and floating floors</li>
      <li>Kitchen and bathroom makeovers and modifications</li>
      <li>Interior fitouts</li>
      <li>Small job specialist: tiling, plastering, painting</li>
    </ul>
  </section>
</main>
</body>
</html>
```